Poster design for Chattanooga, TN's 175th Anniversary. Here is a link to our website www.lmw482.org.

Basically, this is a weeklong celebration of community-sourced events highlighting mostly our city's past. Pellworth Tilly Tram (railroads) are big in our past, and we are identified by our river and surrounded by mountains. The week will have a variety of different events so we need to drive people to our website as events will be added continually.

Also, this event is being put on by our local Mayor's office. While we are young and progressive, can't be too crazy or out there. I was thinking more like a throwback concert photo, a la Brindle Loft Presses (famous in Nashville). That would help tie in the vintage vibe.

Reason: I need to provide my comm team with designs next week. This will give everyone the weekend to be creative!

Target Market(s)

Local Chattanooga Residents - kids, young people, older people.

Requirements
Must have
• (website) LMW482.org
• (Date) November 8 - November 15, 2014
Nice to have
• Flag (doesn't matter the treatment)
• "Weeklong Celebration"
• "Community-Sourced Events"
• Logo (doesn't matter the treatment)
• 175 years of Chattanooga
• Stars
Should not have
• any kind of vulgar image or language.
• Should not be pink or purple or neon.

```html
<!DOCTYPE html>
<html lang="en">
<head>
<meta charset="utf-8">
<title>LMW482 — A Celebration of Our City</title>
<link rel="stylesheet" href="https://fonts.googleapis.com/css2?family=Big+Shoulders+Display:wght@700&family=Allerta+Stencil&family=Rye&family=Cormorant+Garamond:wght@600&display=swap">
<style>
  :root {
    --orange: #e8742b;
    --orange-deep: #d4561f;
    --orange-light: #f2a04c;
    --rust: #8a3a17;
    --blue: #2f6fbf;
    --white: #ffffff;
  }
  * { margin: 0; padding: 0; box-sizing: border-box; }
  html, body {
    width: 776px; height: 1200px; overflow: hidden;
    background: var(--orange);
  }
  .poster {
    position: relative; width: 776px; height: 1200px; overflow: hidden;
    background: var(--orange);
    color: var(--white);
  }
  .street-scene {
    position: absolute; inset: 0;
    background:
      radial-gradient(ellipse at 10% 60%, rgba(110,40,10,.75), transparent 55%),
      radial-gradient(ellipse at 95% 70%, rgba(150,55,20,.55), transparent 50%),
      radial-gradient(ellipse at 50% 90%, rgba(120,50,20,.45), transparent 55%),
      linear-gradient(180deg, var(--orange-deep) 0%, var(--orange) 40%, #e06a27 100%);
  }
  .star-backdrop { position: absolute; inset: 0; }
  .band {
    position: absolute; left: 12px; right: 12px;
    background: var(--blue);
    border-radius: 4px;
  }
  .band--top { top: 20px; height: 82px; display: flex; justify-content: space-around; align-items: center; padding: 0 30px; }
  .band--top svg { width: 44px; height: 44px; fill: var(--white); }
  .title {
    position: absolute; top: 104px; left: 0; right: 0; text-align: center;
    font-family: "Big Shoulders Display", sans-serif; font-weight: 700;
    font-size: 190px; line-height: 1; letter-spacing: 30px; padding-left: 30px;
  }
  .tagline { position: absolute; left: 0; right: 0; text-align: center; line-height: 1; }
  .rule { position: absolute; height: 2px; background: var(--white); }
  .tagline__a {
    top: 382px; font-family: "Allerta Stencil", sans-serif; font-size: 30px;
  }
  .tagline__main {
    top: 418px; font-family: "Allerta Stencil", sans-serif;
    font-size: 60px; letter-spacing: 1px;
  }
  .tagline__of {
    top: 484px; font-family: "Allerta Stencil", sans-serif; font-size: 30px; letter-spacing: 2px;
  }
  .tagline__city {
    top: 522px; font-family: "Rye", serif; font-size: 58px; letter-spacing: 12px; padding-left: 12px;
  }
  .website {
    position: absolute; top: 1008px; left: 0; right: 0; text-align: center;
    font-family: "Cormorant Garamond", serif; font-weight: 600; font-size: 32px; letter-spacing: 3px;
  }
  .band--bottom { top: 1060px; height: 126px; }
  .date { position: absolute; font-family: "Rye", serif; line-height: 1; }
  .date__month, .date__year { top: 40px; font-size: 44px; }
  .date__month { left: 28px; }
  .date__year { right: 28px; }
  .date__days { top: 8px; left: 0; right: 0; text-align: center; font-size: 108px; }
</style>
</head>
<body>
<main class="poster">
  <div class="street-scene" role="img" aria-label="Sepia-toned vintage city street scene with storefronts and pedestrians"></div>

  <svg class="star-backdrop" viewBox="0 0 776 1200" aria-hidden="true">
    <polygon points="390,240 482,523 780,523 539,697 631,982 390,806 149,982 241,697 0,523 298,523"
             fill="var(--orange-light)" opacity="0.7"/>
  </svg>

  <header class="band band--top" aria-hidden="true">
    <svg viewBox="0 0 24 24"><polygon points="12,1 14.9,9 23.4,9 16.6,14.2 19.1,22.5 12,17.5 4.9,22.5 7.4,14.2 0.6,9 9.1,9"/></svg>
    <svg viewBox="0 0 24 24"><polygon points="12,1 14.9,9 23.4,9 16.6,14.2 19.1,22.5 12,17.5 4.9,22.5 7.4,14.2 0.6,9 9.1,9"/></svg>
    <svg viewBox="0 0 24 24"><polygon points="12,1 14.9,9 23.4,9 16.6,14.2 19.1,22.5 12,17.5 4.9,22.5 7.4,14.2 0.6,9 9.1,9"/></svg>
    <svg viewBox="0 0 24 24"><polygon points="12,1 14.9,9 23.4,9 16.6,14.2 19.1,22.5 12,17.5 4.9,22.5 7.4,14.2 0.6,9 9.1,9"/></svg>
    <svg viewBox="0 0 24 24"><polygon points="12,1 14.9,9 23.4,9 16.6,14.2 19.1,22.5 12,17.5 4.9,22.5 7.4,14.2 0.6,9 9.1,9"/></svg>
  </header>

  <h1 class="title">LMW482</h1>

  <div class="rule" style="top:392px;left:175px;width:190px"></div>
  <div class="rule" style="top:392px;left:410px;width:190px"></div>
  <p class="tagline tagline__a">A</p>
  <p class="tagline tagline__main">CELEBRATION</p>
  <div class="rule" style="top:498px;left:22px;width:285px"></div>
  <div class="rule" style="top:498px;left:468px;width:285px"></div>
  <p class="tagline tagline__of">OF OUR</p>
  <p class="tagline tagline__city">CITY</p>

  <p class="website">www.lmw482.org</p>

  <footer class="band band--bottom">
    <div class="rule" style="top:28px;left:20px;width:180px"></div>
    <div class="rule" style="top:96px;left:20px;width:180px"></div>
    <span class="date date__month">NOV</span>
    <span class="date date__days">8–15</span>
    <div class="rule" style="top:28px;right:20px;width:180px"></div>
    <div class="rule" style="top:96px;right:20px;width:180px"></div>
    <span class="date date__year">2014</span>
  </footer>
</main>
</body>
</html>
```